Need simple and modern looking business card with all my information on one side and logo on the other side
Info :
Company name - VELMAR CONSTRUCTION LLC
Company addres- 418 harbor 87th. Dunmoor park ny 10352
Email- velmarllc@tridomail.Com
Company phone number 555-318-6094
Cell number- 555-742-0583
Web site - velmarllc.Com
My name Gerald tomasino

Target Market(s)

Construction , home improvement, remodeling

Industry/Entity Type

Construction

Contact Information for Business Card

It has to be moder but at the same time simple

Font styles to use
Sans Serif

Colors
0255a3
ffffff
000000
f78f20
b1b1b1
9d9d9d
1b1b1b
33a6d7
ec1f27

Requirements
Must have
• My logo on one side maybe with a some kind of background on the other side all my information
Nice to have
• Some kind of background pictures provided by you .PLEASE HAVE ACCOUNT WITH PIXELVAULT WILL NOT PAY ANY EXTRA FEES .
Should not have
• Any kind of hamer, nails,screws, helmets itp. Please do not copy the other designs come up with something new.

```html
<!DOCTYPE html>
<html lang="en">
<head>
<meta charset="utf-8">
<title>Velmar Construction LLC – Business Card</title>
<link rel="stylesheet" href="https://fonts.googleapis.com/css2?family=Arimo:wght@400;700&display=swap">
<style>
  :root {
    --page-bg: #e6e4e1;
    --card-white: #ffffff;
    --ink: #111111;
    --band-dark: #3a3536;
    --brand-blue: #3e5ea9;
    --brand-green: #a7d36b;
    --dot-yellow: #ffd500;
    --dot-ring: #f7a21b;
    --text-font: "Arimo", Arial, sans-serif;
  }
  * { box-sizing: border-box; margin: 0; padding: 0; }
  html, body { width: 1200px; height: 1200px; overflow: hidden; }
  body {
    background: var(--page-bg);
    font-family: var(--text-font);
    color: var(--ink);
    position: relative;
  }
  .card {
    position: absolute;
    left: 160px;
    width: 880px;
    height: 503px;
    background: var(--card-white);
    overflow: hidden;
    box-shadow: 0 6px 18px rgba(0,0,0,0.18);
  }
  .card--info { top: 66px; }
  .card--logo { top: 631px; }

  /* ---------- info side ---------- */
  .edge-left { position: absolute; left: 0; top: 0; width: 14px; height: 100%; background: var(--band-dark); }
  .block-blue { position: absolute; background: var(--brand-blue); }
  .block-blue--top { left: 24px; top: 34px; width: 306px; height: 112px; }
  .block-blue--bottom { left: 24px; top: 312px; width: 306px; height: 191px; }
  .bar-green { position: absolute; background: var(--brand-green); }
  .bar-green--top { left: 346px; top: 0; width: 62px; height: 60px; }
  .bar-green--bottom { left: 346px; top: 264px; width: 62px; height: 239px; }
  .band-right { position: absolute; right: 0; top: 0; width: 92px; height: 100%; background: var(--band-dark); }
  .dot {
    position: absolute;
    width: 48px; height: 48px;
    border-radius: 50%;
    background: var(--dot-yellow);
    border: 6px solid var(--dot-ring);
  }
  .card--info .dot { left: 766px; top: 56px; }
  .website {
    position: absolute;
    right: 30px; top: 250px;
    transform-origin: right top;
    transform: rotate(90deg) translateX(50%);
    color: #ffffff;
    font-size: 27px;
    letter-spacing: 1px;
    white-space: nowrap;
  }
  .wordmark-small {
    position: absolute;
    left: 60px; top: 180px;
    width: 276px;
    font-weight: 700;
    color: var(--ink);
    padding: 8px 10px;
    line-height: 1;
    white-space: nowrap;
  }
  .wordmark-small .w-main { display: block; font-size: 56px; letter-spacing: 1px; }
  .wordmark-small .w-sub { display: block; font-size: 19px; letter-spacing: 1px; margin-top: 6px; }
  .contact { position: absolute; left: 440px; top: 262px; }
  .contact__name { font-size: 31px; letter-spacing: 1px; margin-bottom: 14px; }
  .contact__address { font-size: 24px; line-height: 1.15; letter-spacing: 0.5px; margin-bottom: 12px; }
  .contact__rows { display: grid; grid-template-columns: 74px 1fr; font-size: 19px; line-height: 1.15; }
  .contact__label { padding-right: 10px; }
  .contact__value { border-left: 1.5px solid var(--ink); padding-left: 8px; }

  /* ---------- logo side ---------- */
  .band-left { position: absolute; left: 0; top: 0; width: 64px; height: 100%; background: var(--band-dark); }
  .stripe { position: absolute; top: 0; height: 100%; }
  .stripe--blue { left: 74px; width: 12px; background: var(--brand-blue); }
  .stripe--green { left: 98px; width: 8px; background: var(--brand-green); }
  .tab {
    position: absolute; left: 0; top: 38px;
    width: 176px; height: 76px;
    background: var(--band-dark);
    border-radius: 0 38px 38px 0;
  }
  .card--logo .dot { left: 116px; top: 52px; }
  .edge-right { position: absolute; right: 0; top: 0; width: 20px; height: 100%; background: var(--band-dark); }
  .wordmark-large {
    position: absolute; left: 170px; top: 210px;
    width: 660px;
    font-weight: 700; color: var(--ink); line-height: 1;
    white-space: nowrap;
  }
  .wordmark-large .w-main { display: block; font-size: 146px; letter-spacing: 2px; }
  .wordmark-large .w-sub { display: block; font-size: 46px; letter-spacing: 3px; margin-top: 14px; }
</style>
</head>
<body>

<section class="card card--info" aria-label="Business card, contact side">
  <div class="edge-left"></div>
  <div class="block-blue block-blue--top"></div>
  <div class="block-blue block-blue--bottom"></div>
  <div class="bar-green bar-green--top"></div>
  <div class="bar-green bar-green--bottom"></div>
  <div class="wordmark-small"><span class="w-main">VELMAR</span><span class="w-sub">CONSTRUCTION LLC</span></div>
  <div class="band-right"></div>
  <div class="dot"></div>
  <div class="website">velmarllc.com</div>
  <div class="contact">
    <p class="contact__name">GERALD TOMASINO</p>
    <p class="contact__address">418 HARBOR 87TH<br>DUNMOOR PARK, NY 10352</p>
    <div class="contact__rows">
      <span class="contact__label">email</span><span class="contact__value">velmarllc@tridomail.com</span>
      <span class="contact__label">office</span><span class="contact__value">555.318.6094</span>
      <span class="contact__label">mobile</span><span class="contact__value">555.742.0583</span>
    </div>
  </div>
</section>

<section class="card card--logo" aria-label="Business card, logo side">
  <div class="band-left"></div>
  <div class="stripe stripe--blue"></div>
  <div class="stripe stripe--green"></div>
  <div class="tab"></div>
  <div class="dot"></div>
  <div class="edge-right"></div>
  <div class="wordmark-large"><span class="w-main">VELMAR</span><span class="w-sub">CONSTRUCTION LLC</span></div>
</section>

</body>
</html>
```